Etiketten-Design für Gin
Zielgruppe
Herstellung von Spirituosen/ Molk UG (haftungsbeschränkt)
Zielgruppe: Vorwiegend Männer von 45 bis 70 Jahre
Aufgabenstellung
Flaschen Etikett Vorder- und Rückseite für Gin
Wortmarke: Dry Gin Molk sollte hervorgehoben sein.
Bedeutung hat für uns auch, dass er aus der Region Rhein-Main kommt.

```html
<!DOCTYPE html>
<html lang="de">
<head>
<meta charset="utf-8">
<title>Dry Gin Molk – Etiketten</title>
<link rel="stylesheet" href="https://fonts.googleapis.com/css2?family=Six+Caps&family=Alfa+Slab+One&family=Oswald:wght@700&display=swap">
<style>
  :root {
    --page: #ffffff;
    --label: #303030;
    --gold: #958462;
  }
  html, body {
    margin: 0;
    padding: 0;
    width: 1200px;
    height: 748px;
    overflow: hidden;
    background: var(--page);
  }
  .canvas {
    position: relative;
    width: 1200px;
    height: 748px;
  }
  .label {
    position: absolute;
    top: 66px;
    width: 283px;
    height: 591px;
    background: var(--label);
  }
  .label--front { left: 201px; }
  .label--back { left: 747px; }
  .label svg {
    position: absolute;
    inset: 0;
    width: 283px;
    height: 591px;
  }
  .display {
    font-family: "Six Caps", "Oswald", sans-serif;
    fill: var(--gold);
  }
  .rule {
    stroke: var(--gold);
    stroke-width: 1.6;
    fill: none;
  }
  .ornament { fill: var(--gold); }
  .facts {
    font-family: "Oswald", sans-serif;
    font-weight: 700;
    fill: var(--gold);
  }
  .description {
    position: absolute;
    left: 8px;
    right: 8px;
    top: 225px;
    margin: 0;
    font-family: "Alfa Slab One", serif;
    font-size: 16px;
    line-height: 26.3px;
    text-align: center;
    text-transform: uppercase;
    color: var(--gold);
  }
  .origin {
    position: absolute;
    left: 0;
    right: 0;
    margin: 0;
    text-align: center;
    font-family: "Oswald", sans-serif;
    font-weight: 700;
    color: var(--gold);
    white-space: nowrap;
  }
  .origin--main { top: 477px; font-size: 14px; letter-spacing: -0.2px; }
  .origin--producer { top: 498px; font-size: 8.5px; }
</style>
</head>
<body>
<main class="canvas">

  <section class="label label--front" aria-label="Vorderseite">
    <svg viewBox="0 0 283 591">
      <defs>
        <path id="front-brand-arc" d="M41 147 Q145 71 250 144"/>
        <path id="front-origin-arc" d="M63 396 Q145 458 223 392"/>
      </defs>
      <path class="rule" d="M17 118 Q145 2 272 118"/>
      <path class="rule" d="M64 160 Q145 86 227 160"/>
      <text class="display" font-size="44">
        <textPath href="#front-brand-arc" startOffset="50%" text-anchor="middle" textLength="240" lengthAdjust="spacingAndGlyphs">DESTILLERIE MOLK</textPath>
      </text>

      <text class="display" x="16" y="309" font-size="122" textLength="256" lengthAdjust="spacingAndGlyphs">DRY GIN MOLK</text>
      <line class="rule" x1="11" y1="313" x2="272" y2="313"/>

      <polygon class="ornament" points="142,352 150,366 142,381 134,366"/>

      <text class="display" font-size="30">
        <textPath href="#front-origin-arc" startOffset="50%" text-anchor="middle" textLength="172" lengthAdjust="spacingAndGlyphs">DISTILLED IN GERMANY</textPath>
      </text>

      <line class="rule" x1="11" y1="521" x2="272" y2="521"/>
      <line class="rule" x1="11" y1="531" x2="51" y2="531"/>
      <line class="rule" x1="11" y1="541" x2="51" y2="541"/>
      <line class="rule" x1="11" y1="550" x2="51" y2="550"/>
      <line class="rule" x1="233" y1="531" x2="272" y2="531"/>
      <line class="rule" x1="233" y1="541" x2="272" y2="541"/>
      <line class="rule" x1="233" y1="550" x2="272" y2="550"/>
      <line class="rule" x1="11" y1="559" x2="272" y2="559"/>
      <text class="display" x="86" y="553" font-size="32" textLength="26" lengthAdjust="spacingAndGlyphs">35 CL</text>
      <polygon class="ornament" points="142,531 148,541 142,551 136,541"/>
      <text class="display" x="167" y="553" font-size="32" textLength="50" lengthAdjust="spacingAndGlyphs">45 % VOL.</text>
    </svg>
  </section>

  <section class="label label--back" aria-label="Rückseite">
    <svg viewBox="0 0 283 591">
      <defs>
        <path id="back-brand-arc" d="M43 99 Q142 27 246 97"/>
      </defs>
      <path class="rule" d="M21 75 Q142 -35 266 75"/>
      <path class="rule" d="M65 115 Q142 45 221 115"/>
      <text class="display" font-size="42">
        <textPath href="#back-brand-arc" startOffset="50%" text-anchor="middle" textLength="232" lengthAdjust="spacingAndGlyphs">DESTILLERIE MOLK</textPath>
      </text>

      <polygon class="ornament" points="49,145 54,153 49,161 44,153"/>
      <text class="display" x="87" y="172" font-size="58" textLength="119" lengthAdjust="spacingAndGlyphs">DRY GIN MOLK</text>
      <line class="rule" x1="86" y1="174" x2="207" y2="174"/>
      <polygon class="ornament" points="246,145 251,153 246,161 241,153"/>
      <text class="display" x="110" y="206" font-size="27" textLength="72" lengthAdjust="spacingAndGlyphs">WESTERN DRY GIN</text>

      <line class="rule" x1="11" y1="521" x2="272" y2="521"/>
      <line class="rule" x1="11" y1="531" x2="51" y2="531"/>
      <line class="rule" x1="11" y1="541" x2="51" y2="541"/>
      <line class="rule" x1="11" y1="550" x2="51" y2="550"/>
      <line class="rule" x1="233" y1="531" x2="272" y2="531"/>
      <line class="rule" x1="233" y1="541" x2="272" y2="541"/>
      <line class="rule" x1="233" y1="550" x2="272" y2="550"/>
      <line class="rule" x1="11" y1="559" x2="272" y2="559"/>
      <text class="facts" x="61" y="547" font-size="14">35 cl</text>
      <text class="facts" x="230" y="547" font-size="14" text-anchor="end">45 % Vol.</text>
    </svg>

    <p class="description">Ein erlesener Gin aus<br>dem Herzen des<br>Rhein-Main Gebietes, im<br>Kupferkessel 2-fach<br>destilliert.<br>Er schmeckt deutlich<br>nach Zitrusnoten, leicht<br>pfeffrig und enthält<br>subtil herbe Botanicals.</p>
    <p class="origin origin--main">Destilliert und abgefüllt in Deutschland.</p>
    <p class="origin origin--producer">Erzeugerbetrieb: Molk UG (haftungsbeschränkt), D-63000 Lindenau</p>
  </section>

</main>
</body>
</html>
```